Website Redesign for Accommodation Directory

We need a redesign for bluepinelodgefinder.example
The new design needs to include a banner with overlaid text and a 'get started now' button. The overlaid text could be 'Find Hotels in Auckland, New Zealand' for example.
The new design needs to include:
- primary navigation in header
- an accommodation search (left or right column)
- a secondary navigation menu (under the search).
We will need the following font styles (including links for each) defined also please:
h1, h2, h3, h4, h5, h6, p, ul, ol, address, pre

```html
<!DOCTYPE html>
<html lang="en">
<head>
<meta charset="utf-8">
<title>bluepinelodgefinder.example</title>
<link href="https://fonts.googleapis.com/css2?family=Arimo:wght@400;700&family=Open+Sans:wght@600;700&family=Anton&display=swap" rel="stylesheet">
<style>
:root{
  --red:#e0141c;
  --red-dark:#b30d12;
  --ink:#222;
  --text:#333;
  --grey-band:#e6e6e6;
  --grey-mid:#9a9a9a;
  --grey-dark:#444;
  --footer:#8c8c8c;
  --white:#fff;
}
*{box-sizing:border-box;margin:0;padding:0}
html,body{width:801px;height:1200px;overflow:hidden}
body{position:relative;background:var(--white);font-family:"Arimo",Arial,sans-serif;color:var(--text);font-size:10px}
.abs{position:absolute}

/* header */
.header{left:0;top:0;width:801px;height:72px;background:linear-gradient(#fff,#ececec)}
.brand{left:16px;top:20px;display:flex;align-items:center;gap:6px}
.brand-mark{width:26px;height:26px;background:var(--red)}
.brand-name{font-size:22px;color:var(--grey-dark);font-weight:400;letter-spacing:-.3px}
.top-links{right:16px;top:13px;font-size:10px;color:#555}
.phone{right:21px;top:42px;font-size:12px;font-weight:700;color:var(--red);letter-spacing:.4px}

/* primary nav */
.nav{left:0;top:72px;width:801px;height:39px;background:linear-gradient(#fafafa,#dcdcdc);border-top:3px solid #333}
.nav ul{list-style:none;position:relative;height:100%}
.nav li{position:absolute;top:0;height:36px;line-height:36px;font-size:10px;color:#111;text-align:center}
.nav li.active{border-top:4px solid var(--red);margin-top:-3px;background:linear-gradient(#e6e6e6,#cfcfcf)}
.nav li.open{background:linear-gradient(#ccc,#b8b8b8)}
.nav .sep{position:absolute;top:4px;width:1px;height:28px;background:#bbb}
.dropdown{left:347px;top:111px;width:170px;height:101px;background:rgba(30,30,30,.92);list-style:none}
.dropdown li{height:24.5px;line-height:24px;padding-left:29px;color:#ddd;font-size:9.5px;border-bottom:1px solid #3a3a3a;position:relative}
.dropdown li .chev{position:absolute;right:10px;top:0;color:var(--red)}

/* banner */
.banner{left:0;top:111px;width:801px;height:301px;background:linear-gradient(100deg,#4a3a2c 0%,#8a7260 30%,#c8b49a 50%,#6a5848 75%,#c9b18a 100%)}
.banner-shadow{left:0;top:412px;width:801px;height:20px;background:linear-gradient(rgba(0,0,0,.25),rgba(0,0,0,0))}
.arrow-btn{top:232px;width:52px;height:52px;background:rgba(255,255,255,.35)}
.caption{left:498px;top:252px;width:303px;height:126px;background:rgba(255,255,255,.6);border:1px solid rgba(255,255,255,.9)}
.caption .lead{left:46px;top:10px;font-family:"Open Sans",sans-serif;font-weight:700;font-size:25px;color:var(--red)}
.caption .place{left:38px;top:38px;font-family:"Anton",sans-serif;font-size:34px;line-height:34px;color:#000;text-align:right;width:260px;letter-spacing:1px}
.cta{left:616px;top:367px;width:156px;height:36px;background:linear-gradient(var(--red),var(--red-dark));border-radius:3px;box-shadow:0 2px 4px rgba(0,0,0,.4);color:#fff;font-family:"Open Sans",sans-serif;font-weight:700;font-size:14px;display:flex;align-items:center;gap:8px;padding-left:9px}
.cta-icon{width:18px;height:18px;border-radius:50%;background:#f5a020;display:flex;align-items:center;justify-content:center}

/* sidebar */
.search-panel{left:16px;top:445px;width:223px;height:145px;background:linear-gradient(#b5b5b5,#9d9d9d);border:1px solid #ccc}
.panel-title{font-family:"Open Sans",sans-serif;font-weight:700;font-size:15px;color:#fff;text-shadow:0 1px 2px rgba(0,0,0,.4)}
.select{left:16px;width:191px;height:22px;background:#eee;border:1px solid #888;font-size:9.5px;line-height:20px;padding-left:6px;color:#555}
.select .btn{position:absolute;right:0;top:0;width:26px;height:20px;background:#666}
.btn-dark{height:21px;background:linear-gradient(#777,#444);color:#fff;font-size:9.5px;line-height:21px;text-align:center;border:1px solid #ccc}
.side-head{left:16px;width:223px;height:38px;background:linear-gradient(#777,#4c4c4c);border-radius:3px;color:#fff;font-family:"Open Sans",sans-serif;font-weight:700;font-size:15px;line-height:38px;padding-left:15px}
.side-box{left:20px;width:215px;border:1px solid #ccc;background:#fff}
.tertiary{list-style:none}
.tertiary li{height:19.2px;line-height:19px;padding-left:46px;font-size:9.5px;color:#222;position:relative}
.tertiary li::before{content:"";position:absolute;left:31px;top:7px;width:6px;height:6px;border-radius:50%;background:var(--red)}
.tertiary li.current{background:#ddd}
.email{left:8px;top:10px;width:147px;height:22px;background:#eee;border:1px solid #bbb;font-size:9.5px;line-height:20px;padding-left:6px;color:#555}

/* main */
h1.section,h2.section{font-family:"Arimo",sans-serif;font-weight:400;color:var(--ink);font-size:20.5px}
.card{top:479px;width:170px;height:144px;border:1px solid #ccc;background:linear-gradient(#fff,#ececec);padding:3px}
.card .photo{width:162px;height:78px;background:linear-gradient(135deg,#6b4a2a,#c89a5a 50%,#7a3020)}
.card p{font-size:9.5px;line-height:16px;color:#333;padding:5px 6px 0}
.card a{color:var(--red);text-decoration:none;float:right}
.intro{left:262px;top:674px;width:515px;font-size:12.3px;line-height:16px;color:var(--red)}
.body-copy{left:264px;top:735px;width:513px;font-size:9.4px;line-height:16px;color:#222}
.body-copy p{margin-bottom:16px}

/* testimonials */
.t-head{left:30px;top:972px;font-size:15px;font-weight:700;color:#111}
.pager{top:971px;width:20px;height:20px;border-radius:50%;border:1px solid #aaa;background:#fff;display:flex;align-items:center;justify-content:center}
.t-band{left:0;top:997px;width:801px;height:109px;background:var(--grey-band)}
.t-item{top:1013px;width:240px}
.avatar{position:absolute;left:0;top:0;width:68px;height:72px;background:linear-gradient(#cfcfcf,#8a8a8a);border:3px solid #fff;box-shadow:0 1px 2px rgba(0,0,0,.3)}
.t-item .date{position:absolute;left:79px;top:1px;color:var(--red);font-size:9.5px;font-weight:700}
.t-item .quote{position:absolute;left:79px;top:21px;font-size:9.5px;line-height:15px;color:#333;width:170px}
.t-item .who{position:absolute;left:79px;top:60px;font-size:9.5px;color:#111}

/* footer */
.foot-nav{left:0;top:1106px;width:801px;height:34px;background:linear-gradient(#d6d6d6,#c4c4c4);border-top:3px solid #aaa}
.foot-nav span{position:absolute;top:10px;font-size:9.5px;color:#111;transform:translateX(-50%)}
.foot{left:0;top:1140px;width:801px;height:60px;background:var(--footer)}
.foot .legal{position:absolute;left:0;width:801px;text-align:center;font-size:9.5px;color:#222}
.social{top:17px;width:27px;height:27px;border-radius:4px}
</style>
</head>
<body>

<header class="abs header">
  <div class="abs brand"><span class="brand-mark"></span><span class="brand-name">bluepinelodgefinder</span></div>
  <div class="abs top-links">Free Insurance Quotes | Free Website Statistics | Company Reviews</div>
  <div class="abs phone">Phone : 040 5550 123</div>
</header>

<nav class="abs nav" aria-label="Primary">
  <ul>
    <li class="active" style="left:16px;width:98px">Home</li><span class="sep" style="left:114px"></span>
    <li style="left:114px;width:103px">About Us</li><span class="sep" style="left:217px"></span>
    <li style="left:217px;width:130px">Add Your Property</li><span class="sep" style="left:347px"></span>
    <li class="open" style="left:347px;width:82px">Supplier</li><span class="sep" style="left:429px"></span>
    <li style="left:429px;width:83px">Log in</li><span class="sep" style="left:512px"></span>
    <li style="left:512px;width:105px">Accommodation</li><span class="sep" style="left:617px"></span>
    <li style="left:617px;width:75px">Search</li><span class="sep" style="left:692px"></span>
    <li style="left:692px;width:88px">Contact Us</li>
  </ul>
</nav>

<div class="abs banner" role="img" aria-label="Photo of a hotel bedroom with a large bed and bedside lamp"></div>
<ul class="abs dropdown">
  <li>Contrary to popular<span class="chev">›</span></li>
  <li>Contrary to popular</li>
  <li>Contrary to popular<span class="chev">›</span></li>
  <li>Contrary to popular</li>
</ul>
<div class="abs banner-shadow"></div>
<div class="abs arrow-btn" style="left:25px"><svg width="52" height="52"><path d="M30 16 L21 26 L30 36" stroke="#555" stroke-width="4" fill="none"/></svg></div>
<div class="abs caption">
  <div class="abs lead">Find Hotels in</div>
  <div class="abs place">AUCKLAND,<br>NEW ZEALAND</div>
</div>
<div class="abs arrow-btn" style="left:741px"><svg width="52" height="52"><path d="M22 16 L31 26 L22 36" stroke="#555" stroke-width="4" fill="none"/></svg></div>
<div class="abs cta"><span class="cta-icon"><svg width="12" height="12"><path d="M2 6 H9 M6 3 L9 6 L6 9" stroke="#fff" stroke-width="2" fill="none"/></svg></span>Get Started Now</div>

<aside>
  <div class="abs search-panel">
    <div class="abs panel-title" style="left:21px;top:8px">Search Accommodation</div>
    <div class="abs select" style="top:47px">All Countries<span class="btn"></span></div>
    <div class="abs select" style="top:79px">All Categories<span class="btn"></span></div>
    <div class="abs btn-dark" style="left:150px;top:107px;width:57px">Search</div>
  </div>

  <div class="abs side-box" style="top:600px;height:270px"></div>
  <div class="abs side-head" style="top:600px">Tertiary Navigation</div>
  <ul class="abs tertiary" style="left:21px;top:637px;width:213px">
    <li class="current">Apartments</li><li>Backpackers</li><li>Batch</li><li>Beach House</li>
    <li>Bed And Breakfasts</li><li>Camping Sites</li><li>Caravan Park</li><li>Holiday Homes</li>
    <li>Hostels</li><li>Hotels</li><li>Lodges</li><li>Motels</li>
  </ul>

  <div class="abs side-box" style="top:900px;height:52px">
    <div class="abs email">Your e-Mail I.D here</div>
    <div class="abs btn-dark" style="left:155px;top:12px;width:56px">Search</div>
  </div>
  <div class="abs side-head" style="top:866px">Newsletter</div>
</aside>

<main>
  <h2 class="abs section" style="left:262px;top:447px">Featured Accomodations</h2>
  <div class="abs card" style="left:264px"><div class="photo" role="img" aria-label="Photo of a warm-lit hotel room"></div><p>Lorem Ipsum is simply dummy text of the printing and typesetting industry <a href="#">read more</a></p></div>
  <div class="abs card" style="left:440px"><div class="photo" role="img" aria-label="Photo of a hotel room with red bedspread"></div><p>Lorem Ipsum is simply dummy text of the printing and typesetting industry <a href="#">read more</a></p></div>
  <div class="abs card" style="left:614px"><div class="photo" role="img" aria-label="Photo of a lounge with sofas"></div><p>Lorem Ipsum is simply dummy text of the printing and typesetting industry <a href="#">read more</a></p></div>

  <h1 class="abs section" style="left:262px;top:639px">Welcome To Our Site</h1>
  <p class="abs intro">You’ve come to the right place to find Accommodation in Any Country whether it’s a hotel, motel, backpackers, bed and breakfast or beach house you're after you'll find just what you need to enjoy your stay in Any Country.</p>
  <div class="abs body-copy">
    <p>With much to choose from you'll want to find a place that meets your needs. Our accommodation search tool will help you find the perfect place, regardless of what your price, location or style requirements might be.</p>
    <p>Our Any Country accommodation directory is perfect for times when you've scored cheap flights, desperately need last-minute accommodation or are just planning your next holiday or business trip to Any Country.</p>
    <p>With a great selection of Accommodation options in Any Country from cheap nights staying in budget accommodation to 5-star luxury Any Country hotels, so you can really treat yourself, you'll find it all here.</p>
    <p>Using this Any Country Accommodation search tool you'll quickly find a great place to stay offered by providers you can trust and depend on to make sure you get a good night's sleep. From well-known hotel chains to popular beach houses with rave reviews, it's easy to locate welcoming hospitality in Any Country.</p>
  </div>
</main>

<section>
  <h3 class="abs t-head">Testimonials</h3>
  <div class="abs pager" style="left:725px"><svg width="10" height="10"><path d="M7 1 L3 5 L7 9" stroke="#222" stroke-width="2" fill="none"/></svg></div>
  <div class="abs pager" style="left:750px"><svg width="10" height="10"><path d="M3 1 L7 5 L3 9" stroke="#222" stroke-width="2" fill="none"/></svg></div>
  <div class="abs t-band"></div>
  <div class="abs t-item" style="left:38px"><div class="avatar" role="img" aria-label="Reviewer portrait placeholder"></div><span class="date">22-09-2011</span><p class="quote">Lorem Ipsum is simply dummy text of the printing and typesetting industry.</p><span class="who">mr. Daniel Reed (California)</span></div>
  <div class="abs t-item" style="left:286px"><div class="avatar" role="img" aria-label="Reviewer portrait placeholder"></div><span class="date">22-09-2011</span><p class="quote">Lorem Ipsum is simply dummy text of the printing and typesetting industry.</p><span class="who">mr. Daniel Reed (California)</span></div>
  <div class="abs t-item" style="left:534px"><div class="avatar" role="img" aria-label="Reviewer portrait placeholder"></div><span class="date">22-09-2011</span><p class="quote">Lorem Ipsum is simply dummy text of the printing and typesetting industry.</p><span class="who">mr. Daniel Reed (California)</span></div>
</section>

<footer>
  <div class="abs foot-nav">
    <span style="left:71px">Home</span><span style="left:165px">About Us</span><span style="left:282px">Add Your Property</span><span style="left:387px">Supplier</span><span style="left:473px">Log in</span><span style="left:564px">Accommodation</span><span style="left:654px">Search</span><span style="left:735px">Contact Us</span>
  </div>
  <div class="abs foot">
    <p class="legal" style="top:16px">Terms and Conditions | Privacy Policy</p>
    <p class="legal" style="top:34px">All © Copyrights .bluepinelodgefinder . Reserved</p>
    <span class="abs social" style="left:681px;background:#3b5ea8"></span>
    <span class="abs social" style="left:713px;background:#3aa6dc"></span>
    <span class="abs social" style="left:745px;background:#f29222"></span>
  </div>
</footer>

</body>
</html>
```